Business Card Design

I used to run a Mountaineering school and am getting back into business and just want a generic type card with an adventure theme. Core activities will be mountaineering, rock climbing, canyoning, expeditions, cross country skiing,

Industry/Entity Type

School

Contact Information for Business Card

Colin Ashby Adventure Guide
email: tallpinecolin@mailvane.net
+61472 836 915.

```html
<!DOCTYPE html>
<html lang="en">
<head>
<meta charset="utf-8">
<title>Colin Ashby – Adventure Guide Business Card</title>
<link href="https://fonts.googleapis.com/css2?family=Lato:wght@300;400&family=Open+Sans:wght@400;600&display=swap" rel="stylesheet">
<style>
  :root {
    --page-bg: #e9e7e4;
    --card-white: #f7f7f7;
    --card-white-shade: #e4e4e4;
    --name-grey: #7b716c;
    --accent-blue: #3ba5df;
    --band-taupe: #6f625c;
    --deep-blue: #0c2f69;
    --mid-blue: #1d5fa0;
    --light-blue: #5cbcec;
    --text-white: #ffffff;
  }
  * { margin: 0; padding: 0; box-sizing: border-box; }
  html, body { width: 1200px; height: 1023px; overflow: hidden; }
  body {
    background: var(--page-bg);
    position: relative;
    font-family: "Open Sans", Arial, sans-serif;
  }
  .business-card {
    position: absolute;
    left: 120px;
    top: 237px;
    width: 960px;
    height: 548px;
    border-radius: 26px;
    overflow: hidden;
    box-shadow: 0 18px 40px rgba(0,0,0,0.22);
  }
  .card-header {
    position: absolute;
    left: 0; top: 0;
    width: 100%; height: 236px;
    background: linear-gradient(180deg, var(--card-white) 0%, var(--card-white-shade) 100%);
  }
  .brand-name {
    position: absolute;
    left: 56px; top: 52px;
    font-family: "Lato", Arial, sans-serif;
    font-weight: 300;
    font-size: 104px;
    line-height: 1;
    color: var(--name-grey);
    letter-spacing: 1px;
    white-space: nowrap;
  }
  .brand-tagline {
    position: absolute;
    left: 150px; top: 162px;
    font-family: "Lato", Arial, sans-serif;
    font-weight: 400;
    font-size: 52px;
    line-height: 1;
    color: var(--accent-blue);
    white-space: nowrap;
  }
  .activity-band {
    position: absolute;
    left: 0; top: 236px;
    width: 100%; height: 34px;
    background: var(--band-taupe);
    color: var(--text-white);
    font-size: 19px;
    line-height: 34px;
    padding-left: 86px;
    letter-spacing: 0.3px;
    white-space: nowrap;
  }
  .card-body {
    position: absolute;
    left: 0; top: 270px;
    width: 100%; height: 278px;
    background: linear-gradient(160deg, var(--light-blue) -20%, var(--mid-blue) 35%, var(--deep-blue) 100%);
  }
  .person {
    position: absolute;
    left: 80px; top: 130px;
  }
  .person-name {
    font-weight: 600;
    font-size: 30px;
    color: var(--light-blue);
    letter-spacing: 1px;
    white-space: nowrap;
  }
  .person-role {
    font-size: 19px;
    color: var(--text-white);
    margin-top: 2px;
  }
  .divider {
    position: absolute;
    left: 392px; top: 14px;
    width: 1px; height: 160px;
    background: rgba(255,255,255,0.45);
  }
  .contact-list {
    position: absolute;
    left: 414px; top: 20px;
    list-style: none;
  }
  .contact-item {
    display: flex;
    align-items: center;
    gap: 14px;
    font-size: 22px;
    color: var(--text-white);
    height: 42px;
    white-space: nowrap;
  }
  .contact-icon {
    width: 24px; height: 24px;
    border-radius: 4px;
    background: var(--light-blue);
    display: flex;
    align-items: center;
    justify-content: center;
    flex: none;
  }
</style>
</head>
<body>
  <div class="business-card">
    <div class="card-header">
      <div class="brand-name">Colin Ashby</div>
      <div class="brand-tagline">Adventure Guide</div>
    </div>
    <div class="activity-band">Mountaineering | Rock Climbing | Canyoning | Expeditions | Cross Country Skiing</div>
    <div class="card-body">
      <div class="person">
        <div class="person-name">OWEN HALE</div>
        <div class="person-role">Director</div>
      </div>
      <div class="divider"></div>
      <ul class="contact-list">
        <li class="contact-item">
          <span class="contact-icon">
            <svg width="14" height="14" viewBox="0 0 14 14"><path d="M3 1 L5.5 1 L6.5 4 L5 5.2 Q6.2 7.8 8.8 9 L10 7.5 L13 8.5 L13 11 Q12.5 13 10.5 13 Q1 12 1 3.5 Q1 1.5 3 1 Z" fill="#0c2f69"/></svg>
          </span>
          +61472 836 915
        </li>
        <li class="contact-item">
          <span class="contact-icon">
            <svg width="14" height="14" viewBox="0 0 14 14"><rect x="1" y="3" width="12" height="8" rx="1" fill="#0c2f69"/><path d="M1.5 3.5 L7 8 L12.5 3.5" stroke="#5cbcec" stroke-width="1.2" fill="none"/></svg>
          </span>
          tallpinecolin@mailvane.net
        </li>
        <li class="contact-item">
          <span class="contact-icon">
            <svg width="14" height="14" viewBox="0 0 14 14"><path d="M7 13 Q2.5 7.5 2.5 5 A4.5 4.5 0 0 1 11.5 5 Q11.5 7.5 7 13 Z" fill="#0c2f69"/><circle cx="7" cy="5" r="1.6" fill="#5cbcec"/></svg>
          </span>
          48 Granite Ridge Road, Kestrel Bay, NSW
        </li>
      </ul>
    </div>
  </div>
</body>
</html>
```